120ml Jar Label — Masculine Cosmetic Foot Balm for Cracked, Hardworking Heels

We need a print-ready wraparound label for a 120ml jar — a brown/amber glass jar with a black metal screw lid (file photo attached).

--DO NOT PUT A BARCODE ON THE LABEL PLEASE--
**PLEASE READ "PLAN HUDDLE PROJECT BRIEF FINAL.MD" IN ATTACHED FILES IF YOU ARE SUBMITTING A DESIGN.**

The label is 190mm wide × 40mm high.
We need files to be in an .ai format with a 2mm bleed at the end.
Social media handle: @bramblekeepnz (facebook, instagram and tiktok)

Bramble Keep is a New Zealand foot-care brand making practical, no-nonsense products for hardworking men whose jobs wreck their feet. Our flagship product, Ridge Mender Balm, helps fix thick, cracked, hardworking skin.

Brand color scheme and overview is all in the brief file. You may add some brand aligned colors outside of the specified hex codes as you see fit to make a great design. Feel free to remove the "Bramble Keep" text from the logo so Bramble Keep is not doubled up on the front of the label

The tone we want: direct, rugged, and credible — like a workwear brand, not a spa brand. Most cracked-heel products on the market lean soft and feminine; we want to stand apart by looking like a serious fix for a real problem, made in New Zealand.

Full legal requirements for New Zealand cosmetic labelling (ingredients, directions, net contents, origin, etc.) are listed in the attached brief document — these are non-negotiable and must stay legible.

Please see the label attached "Label spacing guide" for this project's rough spacing guide. This label is the same size and sits well on the jar. This label doesn't need to be spaced quite as much as the Verin Label

I want to run the design for a week - I feel 7 days is a good amount of time for designers to see the work, digest the brief and create something remarkable and memorable for Bramble Keep.

Target Market(s)

Working men in New Zealand whose jobs or lifestyle put heavy wear on their feet — tradies, farmers, hospital/shift workers, hunters, and outdoors people. Practical, value-driven buyers rather than luxury skincare shoppers.

Industry/Entity Type

Beauty / Health & Wellness / Cosmetics

Font styles to use
Sans Serif
Other font styles liked:
• Montserrat (bold, headings), Inter (regular, body)

Colors
00AB8E
00BBA5
67D7C9
C6EFE9
E9F9F6
FFC000
F8CF3A
FAE287
FDF2CF
FEFAEE

Requirements
Must have
• All NZ cosmetic labelling requirements from the attached brief (product name, tag line, net contents, ingredients, directions, storage, made in NZ) — legible and complete, not omitted for aesthetics Fits 190mm × 40mm wraparound format for a 120ml brown jar with black lid Uses our existing brand colors: Deep Olive #3C4A34, Bone White #F4EFE6, Terracotta Clay #C1683D, and Warm Grey #4A4540 (exact palette in attached brief) Uses Montserrat (headings) and Inter (body) or close equivalents Incorporates our existing shield-and-wing logo (attached) Brand name and product name clearly readable from a normal shelf/bathroom-cabinet distance
Nice to have
• A style that could extend into a hero/product photo later, similar to the NZ-hills-backdrop look on our website (screenshot attached) — not required for the label itself, just good to keep in mind Original icon work (e.g. a small soak/apply/sock icon set) if it fits the rugged brand feel A design that could work as a small back-label/wraparound split if the front can't fit everything at a readable size
Should not have
• No pastel colors, floral motifs, or delicate script fonts — this should never look like spa/luxury skincare. Don't introduce new brand colors outside the palette provided other than black.

```html
<!DOCTYPE html>
<html lang="en">
<head>
<meta charset="utf-8">
<title>Bramble Keep — Ridge Mender Balm Label</title>
<link href="https://fonts.googleapis.com/css2?family=Inter:wght@400;600&family=Montserrat:wght@500;700&display=swap" rel="stylesheet">
<style>
  :root {
    --backdrop: #dad7d5;
    --olive: #3d4b35;
    --olive-light: #5e6a52;
    --terracotta: #c1683d;
    --bone: #f4efe6;
    --sage: #8d9b80;
  }
  * { margin: 0; padding: 0; box-sizing: border-box; }
  html, body {
    width: 1200px; height: 800px; overflow: hidden;
    background: var(--backdrop);
  }
  .label {
    position: absolute; left: 40px; top: 282px;
    width: 1120px; height: 235px;
    background: var(--olive);
    color: var(--bone);
    font-family: "Inter", Arial, sans-serif;
    overflow: hidden;
  }
  .label__band {
    position: absolute; left: 0; width: 100%; height: 8px;
    background: var(--terracotta);
  }
  .label__band--top { top: 0; }
  .label__band--bottom { bottom: 0; }

  .panel-heading {
    font-family: "Inter", Arial, sans-serif;
    font-weight: 600; font-size: 12px; letter-spacing: 0.01em;
    margin-bottom: 6px;
  }
  .panel-text {
    font-size: 12px; line-height: 16.5px; font-weight: 400;
  }

  .directions { position: absolute; left: 30px; top: 40px; width: 285px; }
  .storage { position: absolute; left: 30px; top: 144px; width: 285px; }

  .foot-art {
    position: absolute; left: 322px; top: 8px;
    width: 165px; height: 112px;
  }

  .brand-block {
    position: absolute; left: 400px; top: 28px; width: 318px;
    text-align: center;
  }
  .brand-mark {
    width: 54px; height: 54px; margin: 0 auto 12px;
    border: 3px solid var(--terracotta); border-radius: 50%;
  }
  .brand-name {
    font-family: "Montserrat", Arial, sans-serif;
    font-weight: 700; font-size: 15px; letter-spacing: 0.03em;
    color: var(--bone);
  }
  .product-name {
    margin-top: 22px;
    font-family: "Montserrat", Arial, sans-serif;
    font-weight: 700; font-size: 21px; letter-spacing: 0.01em;
    color: var(--bone);
  }
  .tagline {
    margin-top: 2px;
    font-family: "Montserrat", Arial, sans-serif;
    font-weight: 500; font-size: 14px; letter-spacing: 0.02em;
    color: var(--terracotta);
  }
  .net-contents {
    margin-top: 18px;
    font-family: "Montserrat", Arial, sans-serif;
    font-weight: 500; font-size: 11.5px;
    color: var(--sage);
  }

  .origin {
    position: absolute; left: 740px; top: 136px;
    transform: translate(-50%, -50%) rotate(-90deg);
    white-space: nowrap;
    font-size: 11px; letter-spacing: 0.02em;
    color: var(--sage);
  }

  .ingredients { position: absolute; left: 804px; top: 40px; width: 270px; }
  .website {
    position: absolute; left: 804px; top: 192px;
    font-family: "Montserrat", Arial, sans-serif;
    font-weight: 500; font-size: 15px;
    color: var(--terracotta);
  }
</style>
</head>
<body>
  <section class="label">
    <div class="label__band label__band--top"></div>

    <div class="directions">
      <h2 class="panel-heading">DIRECTIONS:</h2>
      <p class="panel-text">Apply generously to clean, dry feet, focusing on heels and thick or cracked areas. For cracked heels, wear our moisture-locking socks overnight. Use daily.</p>
    </div>

    <div class="storage">
      <h2 class="panel-heading">STORAGE:</h2>
      <p class="panel-text">Keep out of direct sunlight. Best used within six months of opening.</p>
    </div>

    <svg class="foot-art" viewBox="0 0 165 112" role="img" aria-label="Faint illustration of a bare foot and ankle">
      <defs>
        <radialGradient id="footGlow" cx="0.45" cy="0.4" r="0.6">
          <stop offset="0" stop-color="#7c7a5f" stop-opacity="0.55"/>
          <stop offset="1" stop-color="#7c7a5f" stop-opacity="0"/>
        </radialGradient>
      </defs>
      <rect width="165" height="112" fill="url(#footGlow)"/>
    </svg>

    <div class="brand-block">
      <div class="brand-mark"></div>
      <div class="brand-name">BRAMBLE KEEP</div>
      <h1 class="product-name">RIDGE MENDER BALM</h1>
      <div class="tagline">For Hardworking Soles</div>
      <div class="net-contents">120ML</div>
    </div>

    <div class="origin">MADE IN NEW ZEALAND</div>

    <div class="ingredients">
      <h2 class="panel-heading">INGREDIENTS:</h2>
      <p class="panel-text">Shea Butter, Beef Tallow, Beeswax, Grape Seed Oil, Vegetable Glycerin, Lanolin, Panthenol, Gluconolactone &amp; Sodium Benzoate, Manuka Honey, Allantoin, Vitamin E, Tea Tree Essential Oil, Lemon Myrtle Essential Oil, Rosemary Oleoresin Extract.</p>
    </div>

    <div class="website">www.bramblekeep.co.nz</div>

    <div class="label__band label__band--bottom"></div>
  </section>
</body>
</html>
```